Window Cleaning Leaflet

Hi everyone,

I need a leaflet (couldn't find 'leaflet' as an option when begining this project - so one sided only) to send out to coastal properties in South side Melbourne. The Flyer is aimed at high net individuals, mummies, business people etc who own these properties who don't have time to clean the windows themselves (often multiple levels) and want their home looking fabulous in time for Christmas and NY's celebrations.

I would really love a new and original design for a window washing leaflet. something outside of the norm that 'pops' and makes people feel happy when they look at it.

I guess a point of differentiation is that I'm a female working in a mans industry so appeal to mothers looking for someone who is 'reliable, trustworthy and understanding of peoples needs'.

I have made an outline of what I would like included in the leaflet, so if you could please take a look, feel free to change things around, wording and layout etc. If you can make it sound more professional please do so.

I would like the colours to be 'happy' colours, maybe with a silly season theme?

Overall aesthetically pleasing is a must, I find most window cleaning leaflets fairly mundane and boring, please feel free to think outside the box. The more original the better.

Target Market(s)

People who own large Melbourne homes in affluent suburbs, mainly suburbs with a lot of large coastal properties. Generally owned by high net worth individuals who just don't have tme to clean the windows themselves due to their profession or hectic lifestyles but can afford to pay someone else to do it.

Industry/Entity Type

Window Cleaning

Requirements
Must have
• 1) The name of the business - Tilda’s Glass Gleaming Services
• 2) The coupon special and all details attached:
• Small Homes (up to 12 windows) $120
• Medium Homes (up to 16 windows) $180
• Large Homes (up to 20 windows, 2 storeys) $240
• 20% discount
• *Discount applicable to first time customers only.
• *All services include fly screen, sill and tracks cleaned as well as cobweb removal.
• *Houses with more than 20 windows (or two levels) will have an immediate quote provided upon inspection of the property with 20% discount applied.
• *Tilda’s Glass Gleaming Services are fully insured.
• 3) My contact number - 0418 263 591

```html
<!DOCTYPE html>
<html lang="en">
<head>
<meta charset="utf-8">
<title>Tilda’s Glass Gleaming Services – Leaflet</title>
<link rel="stylesheet" href="https://fonts.googleapis.com/css2?family=Maven+Pro:wght@500;600&family=Arimo:ital,wght@0,400;1,700&family=Roboto+Condensed:wght@700&display=swap">
<style>
  :root {
    --backdrop: #6d6d6f;
    --paper: #ffffff;
    --cyan: #00b2da;
    --blue: #0a78c0;
    --pink: #ec4c9d;
    --ink: #1c1c1c;
    --rule: #c9c9c9;
  }
  * { margin: 0; padding: 0; box-sizing: border-box; }
  html, body { width: 864px; height: 1200px; overflow: hidden; }
  body { background: var(--backdrop); position: relative; font-family: "Arimo", Arial, sans-serif; }

  .leaflet {
    position: absolute; left: 77px; top: 96px;
    width: 710px; height: 1007px;
    background: var(--paper); overflow: hidden;
  }

  .hero-photo {
    position: absolute; left: 0; top: 0; width: 710px; height: 470px;
    background:
      linear-gradient(180deg, rgba(255,255,255,0) 60%, #ffffff 100%),
      linear-gradient(120deg, #e9ecea 0%, #f3efe8 35%, #d9c6a8 60%, #eeeae4 80%, #f6f6f4 100%);
  }

  .discount-badge {
    position: absolute; left: 41px; top: 282px;
    width: 174px; height: 174px; border-radius: 50%;
    background: var(--cyan); border: 6px solid #fff;
    box-shadow: 0 4px 10px rgba(0,0,0,.35);
    color: #fff; font-family: "Roboto Condensed", "Arial Narrow", sans-serif;
    text-align: center; transform: rotate(-12deg);
    display: flex; flex-direction: column; justify-content: center;
  }
  .discount-badge .amount { font-size: 62px; line-height: 58px; }
  .discount-badge .label { font-size: 28px; line-height: 30px; }

  .business-name {
    position: absolute; left: 45px; top: 478px;
    font-family: "Maven Pro", sans-serif; font-weight: 500;
    font-size: 53px; line-height: 60px; color: var(--blue);
  }

  .questions {
    position: absolute; left: 44px; top: 624px; width: 470px;
    font-style: italic; font-weight: 700; font-size: 19px; line-height: 24px;
    color: var(--cyan);
  }
  .questions p + p { margin-top: 10px; }

  .pitch {
    position: absolute; left: 44px; top: 724px; width: 440px;
    font-size: 20px; line-height: 24px; color: var(--ink);
  }

  .price-list { position: absolute; left: 553px; top: 441px; width: 120px; }
  .price-card {
    height: 112px; margin-bottom: 12px;
    border: 2px solid var(--rule); border-radius: 9px; overflow: hidden;
    background: #fff; text-align: center;
    font-family: "Roboto Condensed", "Arial Narrow", sans-serif;
  }
  .price-card .top { color: #fff; padding-top: 8px; height: 80px; }
  .price-card .size { font-size: 14px; line-height: 16px; }
  .price-card .price { font-size: 46px; line-height: 52px; }
  .price-card .limit { font-size: 12px; line-height: 13px; color: var(--ink); padding-top: 8px; }
  .price-card.large .limit { padding-top: 3px; }
  .price-card.small .top { background: var(--cyan); }
  .price-card.medium .top { background: var(--blue); }
  .price-card.large .top { background: var(--pink); }

  .call-band {
    position: absolute; left: 0; top: 817px; width: 710px; height: 62px;
    display: flex; font-family: "Roboto Condensed", "Arial Narrow", sans-serif; color: #fff;
  }
  .call-band .invite {
    width: 350px; background: var(--cyan);
    font-size: 18px; line-height: 22px; padding: 9px 0 0 37px;
  }
  .call-band .phone {
    flex: 1; background: var(--blue);
    font-size: 40px; line-height: 62px; padding-left: 16px;
  }

  .terms {
    position: absolute; left: 38px; top: 893px; width: 640px;
    list-style: none; font-size: 13.5px; line-height: 17px; color: var(--ink);
  }
  .terms li { position: relative; padding-left: 12px; margin-bottom: 5px; }
  .terms li::before { content: "*"; position: absolute; left: 0; top: 1px; }
</style>
</head>
<body>
  <main class="leaflet">
    <div class="hero-photo" role="img" aria-label="Photo of a family playing in a bright living room, with a hand drawing a squeegee across the glass"></div>

    <div class="discount-badge">
      <span class="amount">20%</span>
      <span class="label">Discount</span>
    </div>

    <h1 class="business-name">Tilda’s Glass<br>Gleaming Services</h1>

    <div class="questions">
      <p>Do you need your windows cleaned?</p>
      <p>Are you simply too busy as a hard working parent to do it yourself?</p>
    </div>

    <p class="pitch">Tilda’s Glass Gleaming Services provide a reliable, professional service, ensuring that your home will sparkle.</p>

    <div class="price-list">
      <div class="price-card small">
        <div class="top"><div class="size">SMALL HOMES</div><div class="price">$120</div></div>
        <div class="limit">up to 12 windows</div>
      </div>
      <div class="price-card medium">
        <div class="top"><div class="size">MEDIUM HOMES</div><div class="price">$180</div></div>
        <div class="limit">up to 12 windows</div>
      </div>
      <div class="price-card large">
        <div class="top"><div class="size">LARGE HOMES</div><div class="price">$240</div></div>
        <div class="limit">up to 20 windows<br>&amp; 2 storeys</div>
      </div>
    </div>

    <div class="call-band">
      <div class="invite">Call Tilda today and take advantage<br>of our special introductory offer.</div>
      <div class="phone">Tilda : 0418 263 591</div>
    </div>

    <ul class="terms">
      <li>Discount applicable to first time customers only.</li>
      <li>All services include fly screen, sill and tracks cleaned as well as cobweb removal.</li>
      <li>Houses with more than 20 windows (or two levels) will have an immediate quote<br>provided upon inspection of the property with 20% discount applied.</li>
      <li>Tilda’s Glass Gleaming Services are fully insured.</li>
    </ul>
  </main>
</body>
</html>
```